Business Card for Sugared Soiree

I have a logo for my candy buffet business, and need a business card designed using that logo. Sugared Soiree designs and builds beautiful and delicious candy and dessert tables for all kinds of events. The card should be simple, modern, graphic, colorful, and use the Sugared Soiree Logo.

Target Market(s)

The target market is people hosting major parties and events. This includes brides getting married, parents hosting birthday parties/Sweet Sixteen/Bar Mitzvah/quinceanera parties, and companies hosting corporate events.

Industry/Entity Type

Business

Requirements
Must have
• The business card must have the logo, with or without the tag line.

The following information must be on the card:

Dana Whitfield
CEO & Candy Stylist
614.392.5071
dana@sugaredsoiree-example.com
Nice to have
• I like the idea of having multiple colors of the same design so that several people receiving cards will each receive a different color. Perhaps 3-5 colors or variations on a basic card design.

```html
<!DOCTYPE html>
<html lang="en">
<head>
<meta charset="utf-8">
<title>Sugared Soiree – Business Cards</title>
<link rel="stylesheet" href="https://fonts.googleapis.com/css2?family=Source+Sans+3:wght@400;700&family=Oswald:wght@300;400;700&display=swap">
<style>
  :root {
    --page: #ffffff;
    --ink: #ffffff;
    --grape-top: #c022e2;
    --grape-bottom: #8a1fb2;
    --sky-top: #2bbaf6;
    --sky-bottom: #2177bf;
    --dot-blue: #2aa3df;
    --dot-pink: #e4177f;
    --dot-yellow: #f6a93b;
    --dot-green: #0f9448;
    --dot-violet: #6a5aa6;
  }
  * { margin: 0; padding: 0; box-sizing: border-box; }
  html, body {
    width: 1200px; height: 1000px; overflow: hidden;
    background: var(--page);
  }
  .sheet { position: relative; width: 1200px; height: 1000px; }

  .card {
    position: absolute;
    color: var(--ink);
    text-align: center;
    overflow: hidden;
  }
  .card--grape { background: linear-gradient(180deg, var(--grape-top), var(--grape-bottom)); }
  .card--sky { background: linear-gradient(180deg, var(--sky-top), var(--sky-bottom)); }

  .card--grape-front { left: 40px; top: 55px; width: 591px; height: 338px; }
  .card--grape-back  { left: 560px; top: 141px; width: 592px; height: 339px; }
  .card--sky-front   { left: 40px; top: 529px; width: 591px; height: 338px; }
  .card--sky-back    { left: 560px; top: 579px; width: 594px; height: 340px; }

  .brand-name {
    position: absolute; left: 0; right: 0;
    font-family: "Source Sans 3", sans-serif;
    font-weight: 400;
    font-size: 58px;
    line-height: 1;
    letter-spacing: 0.5px;
  }
  .card--grape-front .brand-name { top: 157px; }
  .card--sky-front .brand-name { top: 168px; }

  .tagline {
    position: absolute; left: 101px; width: 390px;
    display: flex; align-items: center; gap: 8px;
    font-family: "Source Sans 3", sans-serif;
    font-size: 13px; white-space: nowrap;
  }
  .tagline::before, .tagline::after {
    content: ""; flex: 1; height: 1.5px; background: var(--ink);
  }
  .card--grape-front .tagline { top: 216px; }
  .card--sky-front .tagline { top: 226px; }

  .confetti-band { position: absolute; display: block; }
  .confetti-band--short { left: 188px; width: 218px; height: 38px; }
  .confetti-band--full { left: 0; width: 100%; height: 36px; }
  .confetti-band--faint { opacity: 0.55; }

  .contact-grape {
    position: absolute; left: 0; right: 0; top: 122px;
    font-family: "Source Sans 3", sans-serif;
    font-size: 19px; line-height: 33px;
  }
  .contact-grape .person { font-weight: 700; font-size: 21px; }
  .contact-grape .divider {
    display: inline-block; width: 1.5px; height: 20px;
    background: var(--ink); margin: 0 6px 0 8px; vertical-align: -3px;
  }
  .contact-grape .role { font-size: 19px; }

  .contact-sky {
    position: absolute; left: 0; right: 0; top: 98px;
    font-family: "Oswald", sans-serif;
  }
  .contact-sky .person { font-weight: 700; font-size: 24px; line-height: 32px; }
  .contact-sky .role { font-weight: 300; font-size: 18px; line-height: 26px; }
  .contact-sky .phone { font-weight: 300; font-size: 21px; margin-top: 14px; line-height: 30px; }
  .contact-sky .email { font-weight: 300; font-size: 20px; margin-top: 12px; line-height: 30px; }
</style>
</head>
<body>
<main class="sheet">
  <svg width="0" height="0" style="position:absolute" aria-hidden="true">
    <defs>
      <linearGradient id="candy-tones" x1="0" y1="0" x2="1" y2="0">
        <stop offset="0" stop-color="#2aa3df"/>
        <stop offset="0.25" stop-color="#e4177f"/>
        <stop offset="0.5" stop-color="#f6a93b"/>
        <stop offset="0.75" stop-color="#0f9448"/>
        <stop offset="1" stop-color="#6a5aa6"/>
      </linearGradient>
    </defs>
  </svg>

  <section class="card card--grape card--grape-front">
    <p class="brand-name">Sugared Soiree</p>
    <p class="tagline">sweet tables for any event</p>
  </section>

  <section class="card card--grape card--grape-back">
    <svg class="confetti-band confetti-band--short" style="top:47px" viewBox="0 0 218 38" role="img" aria-label="Row of candy-coloured dots">
      <rect x="0" y="0" width="218" height="38" rx="19" fill="url(#candy-tones)"/>
    </svg>
    <div class="contact-grape">
      <p><span class="person">Dana Whitfield</span><span class="divider"></span><span class="role">CEO &amp; CANDY STYLIST</span></p>
      <p>614.392.5071</p>
      <p>dana@sugaredsoiree-example.com</p>
    </div>
    <svg class="confetti-band confetti-band--short" style="top:253px" viewBox="0 0 218 38" role="img" aria-label="Row of candy-coloured dots">
      <rect x="0" y="0" width="218" height="38" rx="19" fill="url(#candy-tones)"/>
    </svg>
  </section>

  <section class="card card--sky card--sky-front">
    <svg class="confetti-band confetti-band--full confetti-band--faint" style="top:0" viewBox="0 0 591 36" preserveAspectRatio="none" role="img" aria-label="Border of faint candy-coloured dots">
      <rect x="0" y="0" width="591" height="36" fill="url(#candy-tones)"/>
    </svg>
    <p class="brand-name">Sugared Soiree</p>
    <p class="tagline">sweet tables for any event</p>
    <svg class="confetti-band confetti-band--full confetti-band--faint" style="top:302px" viewBox="0 0 591 36" preserveAspectRatio="none" role="img" aria-label="Border of faint candy-coloured dots">
      <rect x="0" y="0" width="591" height="36" fill="url(#candy-tones)"/>
    </svg>
  </section>

  <section class="card card--sky card--sky-back">
    <svg class="confetti-band confetti-band--full" style="top:0" viewBox="0 0 594 36" preserveAspectRatio="none" role="img" aria-label="Border of candy-coloured dots">
      <rect x="0" y="0" width="594" height="36" fill="url(#candy-tones)"/>
    </svg>
    <div class="contact-sky">
      <p class="person">DANA WHITFIELD</p>
      <p class="role">CEO &amp; CANDY STYLIST</p>
      <p class="phone">614.392.5071</p>
      <p class="email">dana@sugaredsoiree-example.com</p>
    </div>
    <svg class="confetti-band confetti-band--full" style="top:304px" viewBox="0 0 594 36" preserveAspectRatio="none" role="img" aria-label="Border of candy-coloured dots">
      <rect x="0" y="0" width="594" height="36" fill="url(#candy-tones)"/>
    </svg>
  </section>
</main>
</body>
</html>
```